Kiosk Coin Venture: Safe and Secure Cash Money

Front of card: LOGO

Back of card:
$$$ FREE ATM PLACEMENT $$$
BENIFITS OF HAVING AN ATM AT YOUR BUSINESS
FREE ATM and BTM (Bitcoin) installation, maintenance, and loading.
Lower card processing fees
Stimulate more traffic.
Ease of access for customers
Maintain customers inside location.
Higher tips and spending

Contact me for more information!
Name: Tomas Redilla
Phone: (555) 318-7742 - Call or Text
Email: Tomas@VaultLinkpay.example

Contact Information for Business Card

The card should be shape of the logo. Only the back will have all the contact and business details.

Requirements
Must have
• The logo itself will be one side, the card will be the shape of the logo. contact details on back side.

```html
<!DOCTYPE html>
<html lang="en">
<head>
<meta charset="utf-8">
<title>Kiosk Coin Venture – Business Card</title>
<link rel="stylesheet" href="https://fonts.googleapis.com/css2?family=Barlow+Semi+Condensed:wght@600;700&family=Titillium+Web:wght@300;400&display=swap">
<style>
  :root {
    --backdrop: #444444;
    --card: #000000;
    --silver-light: #e6e6e6;
    --silver-mid: #b3b3b3;
    --silver-dark: #8a8a8a;
    --text-main: #ffffff;
    --text-soft: #a9a9a9;
  }
  html, body {
    margin: 0;
    padding: 0;
    width: 1128px;
    height: 1200px;
    overflow: hidden;
    background: var(--backdrop);
  }
  .card-sheet { display: block; width: 1128px; height: 1200px; }
  .headline { font-family: "Barlow Semi Condensed", sans-serif; font-weight: 700; font-size: 44px; fill: var(--silver-light); letter-spacing: 0.5px; }
  .subline { font-family: "Barlow Semi Condensed", sans-serif; font-weight: 600; font-size: 23px; fill: var(--text-soft); }
  .benefit { font-family: "Titillium Web", sans-serif; font-weight: 300; font-size: 27px; fill: var(--text-main); }
  .person-name { font-family: "Titillium Web", sans-serif; font-weight: 300; font-size: 46px; fill: var(--silver-mid); letter-spacing: 1px; }
  .phone { font-family: "Titillium Web", sans-serif; font-weight: 300; font-size: 28px; fill: var(--text-main); }
  .phone-note { font-style: italic; }
  .email { font-family: "Titillium Web", sans-serif; font-weight: 300; font-size: 21px; fill: var(--text-main); }
  .brand-name { font-family: "Titillium Web", sans-serif; font-weight: 400; font-size: 40px; fill: var(--silver-light); letter-spacing: 2px; }
</style>
</head>
<body>
<svg class="card-sheet" viewBox="0 0 1592 1694" xmlns="http://www.w3.org/2000/svg">
  <defs>
    <linearGradient id="vault-fill" x1="0" y1="0" x2="1" y2="1">
      <stop offset="0" stop-color="#d9d9d9"/>
      <stop offset="0.5" stop-color="#a8a8a8"/>
      <stop offset="1" stop-color="#cfcfcf"/>
    </linearGradient>
    <linearGradient id="tab-fill" x1="0" y1="0" x2="1" y2="0">
      <stop offset="0" stop-color="#8a8a8a"/>
      <stop offset="1" stop-color="#e6e6e6"/>
    </linearGradient>
    <clipPath id="front-shape">
      <path d="M314 158 H1135 L1334 218 V600 Q1334 660 1140 757 H314 Q284 757 284 727 V188 Q284 158 314 158 Z"/>
    </clipPath>
    <clipPath id="back-shape">
      <path d="M480 880 H1304 Q1334 880 1334 910 V1450 Q1334 1480 1304 1480 H470 Q284 1400 284 1330 V942 Z"/>
    </clipPath>
  </defs>

  <!-- Back side: details -->
  <g class="card-details">
    <path class="card-body" fill="var(--card)" d="M314 158 H1135 L1334 218 V600 Q1334 660 1140 757 H314 Q284 757 284 727 V188 Q284 158 314 158 Z"/>
    <circle clip-path="url(#front-shape)" cx="1165" cy="560" r="315" fill="url(#vault-fill)" stroke="#777" stroke-width="6" role="img" aria-label="Silver vault door wheel illustration"/>
    <path class="edge-tab" d="M284 584 H300 L316 636 L300 690 H284 Z" fill="url(#tab-fill)"/>

    <text class="headline" x="357" y="250">$$$ FREE ATM PLACEMENT $$$</text>
    <text class="subline" x="357" y="284">BENIFITS OF HAVING AN ATM AT YOUR BUSINESS</text>

    <g class="benefit-list">
      <circle cx="371" cy="345" r="12" fill="var(--silver-mid)"/>
      <text class="benefit" x="401" y="353">FREE ATM &amp; BTM (Bitcoin)</text>
      <line x1="371" y1="365" x2="371" y2="384" stroke="var(--silver-mid)" stroke-width="2"/>
      <text class="benefit" x="401" y="383">installation, maintenance, &amp; loading.</text>
      <circle cx="371" cy="404" r="12" fill="var(--silver-mid)"/>
      <text class="benefit" x="401" y="413">Lower card processing fees</text>
      <line x1="371" y1="425" x2="371" y2="444" stroke="var(--silver-mid)" stroke-width="2"/>
      <text class="benefit" x="401" y="443">Stimulate more traffic.</text>
      <circle cx="371" cy="464" r="12" fill="var(--silver-mid)"/>
      <text class="benefit" x="401" y="473">Ease of access for customers</text>
      <line x1="371" y1="485" x2="371" y2="504" stroke="var(--silver-mid)" stroke-width="2"/>
      <text class="benefit" x="401" y="503">Maintain customers inside location.</text>
      <circle cx="371" cy="522" r="12" fill="var(--silver-mid)"/>
      <text class="benefit" x="401" y="533">Higher tips &amp; spending</text>
    </g>

    <text class="person-name" x="358" y="617">TOMAS REDILLA</text>

    <g class="contact-phone">
      <path d="M362 642 q3 -3 6 0 l3 4 q1 2 -1 4 l-2 2 q3 5 7 8 l2 -2 q2 -2 4 -1 l4 3 q3 3 0 6 l-2 2 q-6 3 -15 -6 q-9 -9 -6 -16 z" fill="var(--text-main)"/>
      <text class="phone" x="396" y="659">(555) 318-7742 <tspan class="phone-note">Call Or Text</tspan></text>
    </g>
    <g class="contact-email">
      <rect x="360" y="674" width="18" height="12" fill="var(--text-main)"/>
      <path d="M360 674 L369 682 L378 674" fill="none" stroke="var(--card)" stroke-width="1.5"/>
      <text class="email" x="396" y="686">Tomas@VaultLinkpay.example</text>
    </g>
  </g>

  <!-- Front side: brand -->
  <g class="card-brand">
    <path class="card-body" fill="var(--card)" d="M480 880 H1304 Q1334 880 1334 910 V1450 Q1334 1480 1304 1480 H470 Q284 1400 284 1330 V942 Z"/>
    <circle clip-path="url(#back-shape)" cx="450" cy="1285" r="318" fill="url(#vault-fill)" stroke="#777" stroke-width="6" role="img" aria-label="Silver vault door wheel illustration"/>
    <circle cx="1045" cy="1110" r="34" fill="none" stroke="var(--silver-light)" stroke-width="4"/>
    <text class="brand-name" x="1045" y="1210" text-anchor="middle">KIOSK COIN</text>
    <text class="brand-name" x="1045" y="1260" text-anchor="middle">VENTURE</text>
  </g>
</svg>
</body>
</html>
```